" não entendi. Nós fazemos laudos de reforma de acordo com a nbr 16.280 para pessoas físicas e condomínios, também trabalhamos para adm de condomínios; fazemos perícias em unidades autonomas para entrega ao cliente, todos os relatórios são registrados em cartório e com ART; e qualquer serviço de engenharia na parte de engenharia. "

```html
<!DOCTYPE html>
<html lang="pt-BR">
<head>
<meta charset="UTF-8">
<title>Papel Timbrado — Vetor Engenharia</title>
<link href="https://fonts.googleapis.com/css2?family=Lato:wght@700&display=swap" rel="stylesheet">
<style>
  :root {
    --backdrop: #ffffff;
    --sheet: #ffffff;
    --brand-red: #b3262a;
    --brand-grey: #4a4a4c;
    --brand-grey-light: #d4d4d6;
    --logo-ink: #4a4a4c;
    --placeholder-ink: #d9d9d9;
  }
  html, body {
    margin: 0;
    padding: 0;
    width: 1200px;
    height: 1200px;
    overflow: hidden;
    background: var(--backdrop);
  }
  .canvas {
    position: relative;
    width: 1200px;
    height: 1200px;
  }
  .letterhead {
    position: absolute;
    left: 173px;
    top: 0;
    width: 854px;
    height: 1200px;
    background: var(--sheet);
    font-family: "Lato", sans-serif;
    overflow: hidden;
  }
  .letterhead__band {
    position: absolute;
    left: 0;
    right: 0;
    height: 40px;
  }
  .letterhead__band--top {
    top: 0;
    background: linear-gradient(90deg, var(--brand-red) 0%, var(--brand-red) 45%, var(--brand-grey) 80%, var(--brand-grey-light) 100%);
  }
  .letterhead__band--bottom {
    bottom: 0;
    background: linear-gradient(270deg, var(--brand-red) 0%, var(--brand-red) 45%, var(--brand-grey) 80%, var(--brand-grey-light) 100%);
  }
  .brand {
    position: absolute;
    left: 684px;
    top: 62px;
    color: var(--logo-ink);
    font-weight: 700;
    line-height: 1;
  }
  .brand__name {
    display: block;
    font-size: 38px;
    letter-spacing: 1px;
  }
  .brand__field {
    display: block;
    font-size: 17px;
    margin-top: 4px;
  }
  .placeholder-title {
    position: absolute;
    left: 0;
    right: 0;
    top: 548px;
    margin: 0;
    text-align: center;
    font-size: 58px;
    font-weight: 700;
    letter-spacing: 1px;
    color: var(--placeholder-ink);
  }
</style>
</head>
<body>
  <main class="canvas">
    <section class="letterhead">
      <div class="letterhead__band letterhead__band--top" role="img" aria-label="Faixa decorativa do cabeçalho em vermelho e cinza"></div>

      <div class="brand">
        <span class="brand__name">VETOR</span>
        <span class="brand__field">engenharia</span>
      </div>

      <h1 class="placeholder-title">PAPEL TIMBRADO</h1>

      <div class="letterhead__band letterhead__band--bottom" role="img" aria-label="Faixa decorativa do rodapé em vermelho e cinza"></div>
    </section>
  </main>
</body>
</html>
```